DPM Marketing Postcard

Design a 2 Sided marketing postcard for our Real estate management caompany. Looking for a professional yet fresh look that will be printed on a 6"x9" glossy flier

Contact information is www.dunkeldmanagement-example.com dunkeldmanagement@dunkeldmail-example.com and 312-480-7193

WE are targeting small condo and town home properties to take on their administrative responsibilities of management

```html
<!DOCTYPE html>
<html lang="en">
<head>
<meta charset="utf-8">
<title>DPM Marketing Postcard</title>
<link href="https://fonts.googleapis.com/css2?family=Montserrat:wght@300;400;500;600;700&family=Roboto+Condensed:wght@800;900&display=swap" rel="stylesheet">
<style>
  :root {
    --navy: #3b4878;
    --navy-deep: #2f3b68;
    --white: #ffffff;
    --ink: #4b5068;
    --backdrop: #e6e6e8;
    --photo-light: #d9d9d9;
    --photo-mid: #9a9a9a;
    --photo-dark: #5f5f5f;
  }
  * { box-sizing: border-box; margin: 0; padding: 0; }
  html, body { width: 1200px; height: 1200px; overflow: hidden; }
  body {
    background: var(--backdrop);
    font-family: "Montserrat", sans-serif;
    position: relative;
  }
  .postcard {
    position: absolute;
    left: 180px;
    width: 840px;
    height: 560px;
    background: var(--white);
    box-shadow: 0 6px 18px rgba(0,0,0,0.15);
    overflow: hidden;
  }
  .postcard--front { top: 30px; }
  .postcard--back { top: 610px; }

  /* Front */
  .front-photo {
    position: absolute; left: 0; top: 0; width: 52%; height: 100%;
    background: linear-gradient(160deg, var(--photo-light) 0%, var(--photo-mid) 45%, var(--photo-dark) 75%, var(--photo-mid) 100%);
  }
  .call-box {
    position: absolute; left: 110px; top: 250px; width: 270px; height: 120px;
    background: var(--navy); padding: 6px;
  }
  .call-box__inner {
    border: 2px solid var(--white); height: 100%;
    display: flex; flex-direction: column; align-items: center; justify-content: center;
    color: var(--white);
  }
  .call-box__label { font-size: 30px; font-weight: 400; line-height: 1.1; }
  .call-box__phone { font-size: 30px; font-weight: 700; line-height: 1.2; }

  .offer-panel {
    position: absolute; left: 48%; top: 0; right: 0; height: 100%;
    background: var(--navy); color: var(--white);
    padding: 26px 34px 20px; text-align: center;
  }
  .offer-panel__company { font-size: 17px; font-weight: 700; letter-spacing: 0.3px; }
  .offer-panel__kicker { font-size: 13px; font-weight: 700; margin-top: 8px; }
  .offer-panel__solution { font-size: 16px; font-weight: 700; margin-top: 6px; }
  .offer-panel__scope { font-size: 14px; font-weight: 400; margin-top: 6px; }
  .rule { height: 3px; background: var(--white); margin: 14px 6px; }
  .price__lead { font-size: 31px; font-weight: 700; line-height: 1.1; }
  .price__sub { font-size: 23px; font-weight: 300; margin-top: 4px; }
  .price__amount { font-size: 42px; font-weight: 700; line-height: 1.15; margin-top: 2px; }
  .price__unit { font-weight: 300; font-size: 34px; }
  .benefit-box {
    border: 3px solid var(--white); padding: 10px 12px;
    display: flex; flex-direction: column; gap: 8px;
  }
  .benefit-box p { font-size: 11.5px; font-weight: 500; line-height: 1.3; }

  /* Back */
  .back-about {
    position: absolute; left: 0; top: 0; width: 55%; bottom: 54px;
    background: var(--navy); color: var(--white);
  }
  .back-about__header {
    background: var(--white); color: var(--navy-deep);
    font-family: "Roboto Condensed", sans-serif; font-weight: 900;
    font-size: 24px; padding: 14px 28px 10px; letter-spacing: 0.2px;
  }
  .back-about__body { padding: 14px 28px 0; }
  .section-label {
    display: inline-block; border: 2px solid var(--white);
    font-family: "Roboto Condensed", sans-serif; font-weight: 800;
    font-size: 14px; letter-spacing: 1px; padding: 3px 10px; margin-bottom: 12px;
  }
  .about-list { list-style: none; display: flex; flex-direction: column; gap: 12px; margin-bottom: 22px; }
  .about-list li { font-size: 14px; font-weight: 400; line-height: 1.3; }

  .back-services {
    position: absolute; left: 55%; top: 0; right: 0; bottom: 54px;
    padding: 22px 26px 0 28px;
  }
  .service-list { list-style: none; display: flex; flex-direction: column; gap: 11px; }
  .service-list li { font-size: 13px; color: var(--ink); line-height: 1.3; }

  .contact-band {
    position: absolute; left: 0; right: 0; bottom: 0; height: 54px;
    background: var(--navy); color: var(--white);
    display: flex; align-items: center; justify-content: center; gap: 12px;
    padding: 0 24px;
    font-size: 12px; font-weight: 600; letter-spacing: 0.2px;
    white-space: nowrap;
  }
  .contact-band span { flex: none; }
</style>
</head>
<body>

<section class="postcard postcard--front">
  <div class="front-photo" role="img" aria-label="Black and white photo of a modern apartment building with stacked glass balconies"></div>
  <div class="call-box">
    <div class="call-box__inner">
      <span class="call-box__label">CALL</span>
      <span class="call-box__phone">312-480-7193</span>
    </div>
  </div>
  <div class="offer-panel">
    <h1 class="offer-panel__company">DUNKELD PROPERTY MANAGEMENT</h1>
    <p class="offer-panel__kicker">COST EFFECTIVE</p>
    <p class="offer-panel__solution">PROPERTY MANAGEMENT SOLUTION</p>
    <p class="offer-panel__scope">for 3-10 unit buildings</p>
    <div class="rule"></div>
    <p class="price__lead">Prices starting</p>
    <p class="price__sub">as low as</p>
    <p class="price__amount">$ 100/<span class="price__unit">month</span></p>
    <div class="rule"></div>
    <div class="benefit-box">
      <p>Utilize our economies of scale to reduce costs across existing services, (trash, insurance, maintenance, etc)</p>
      <p>Eliminate the unfair burden placed on a few owners to do all the work while others free-ride</p>
      <p>Improve communication amongst all owners and board members</p>
      <p>The association’s board of directors maintain all decision-making power</p>
      <p>Utilize our vetted service providers for prompt job completion and fair pricing</p>
    </div>
  </div>
</section>

<section class="postcard postcard--back">
  <div class="back-about">
    <h2 class="back-about__header">DUNKELD PROPERTY MANAGEMENT LLC</h2>
    <div class="back-about__body">
      <span class="section-label">WHO WE ARE</span>
      <ul class="about-list">
        <li>A professional services organization with a focus on small (3-10 unit) residential buildings</li>
        <li>Over 30 years of combined experience in real estate and property management</li>
        <li>Professional, courteous, timely service that is technologically driven</li>
      </ul>
      <span class="section-label">WHY USE DPM?</span>
      <ul class="about-list">
        <li>Owners are rarely suited to manage associations and the burden often falls unfairly on one or two individuals to do all the work</li>
        <li>Low monthly fees tailored to your needs</li>
        <li>The association’s board of directors maintains control of all decision making.</li>
      </ul>
    </div>
  </div>
  <div class="back-services">
    <ul class="service-list">
      <li>Remove the administrative burden from small residential associations</li>
      <li>Utilize economies of scale to lower costs for all owners across a wide range of providers</li>
      <li>Collect all assessments and pay all vendors</li>
      <li>Provide monthly accounting reconciliation reporting</li>
      <li>Provide access to DPM’s client portal with a central repository of all association materials (by-laws, financials, meeting minutes, communications, etc)</li>
      <li>Issue 1099s to all contractors as required by law</li>
      <li>Prepare year-end financial statements</li>
      <li>Lender and legal HOA documents for mortgage companies and sales</li>
    </ul>
  </div>
  <div class="contact-band">
    <span>www.dunkeldmanagement-example.com</span><span>|</span>
    <span>dunkeldmanagement@dunkeldmail-example.com</span><span>|</span>
    <span>312-480-7193</span>
  </div>
</section>

</body>
</html>
```